依頼詳細
社労士、行政書士としての一般的な業務のほか、農地転用や農業参入に力を入れたいとのことでウェブサイトを制作されることになりました。

掲載コンテンツが未定のため、グローバルメニューではいくつかのサブページを想定しておりますが、決定事項ではないため、トップ1ページ、サブ1ページの計2ページのデザイン制作です。
詳細は添付のワイヤーフレームをご覧ください。

▶︎デザインは各ページ、デスクトップ表示とモバイル表示の2つご用意ください。

▶︎モバイル表示時のメニューは、ハンバーガー推奨ですが、他でも可です。

▶︎デスクトップとモバイルの切り替えは、800pxを基準とします。

▶︎フォントはウェブで使用できるフォントに限ります。使用したフォントを明記してください。googleのウェブフォントは使用可。

▶︎テキストやキャッチコピーはアテの状態でかまいませんが、デザイン上必要であれば、仮に書いていただいても可、評価に加味いたします。

▶︎色合いは、緑〜青を基調を希望。 ただし逸脱しても可。

▶︎ご本人の姿は掲載不可のため、ご本人の写真を想定したデザインは避けてください。

▶︎イラスト調は可。

▶︎ロゴのようなものはありませんが、添付の画像を封筒や名刺に使われているので、参考にしてください。(そのまま使っても可。ただしベクターデータなし)

▶︎有料素材を使用する場合は、使用素材のリンクと総額を明記してください。

▶︎事務所内の写真など、現地での撮影を想定したものは、適当な素材を使用の上、素材上にその旨を明記してください。

▶︎納品は、aiデータ希望ですが、psdデータも可とします。

サイトURL
ページ数
2ページ
希望イメージ
シンプル 複雑
単色 カラフル
暗い 明るい
日常 高級
遊び心 厳粛
未来的 伝統的
女性的 男性的
希望する色
緑系、青系、水色系
納品ファイル
• イラストレーター形式 (.ai)
• フォトショップ形式 (.psd)
補足説明
ランサーの皆さま。
お世話になります。

納品は、モバイル表示のデザインもいただきたいですが、
コンペ参加はデスクトップ表示のみでもかまいません。
ぜひ、ふるってご参加のほど、よろしくお願いいたします。
ご提案いただきましたランサーの皆さま

このたびは、素敵なご提案をいただき、まことにありがとうございます。
弊社都合で申し訳ありませんが、選定会議の都合上、決定の選択は10月16日(金)以降にさせていただきます。
お時間いただきますが、よろしくお願いいたします。
■ 選んだ理由

写真の選択が素晴らしく、また機能としても整ってみえました。
弊社もお客様も満場一致でしたので、採択させていただきました。

■ 提案者全員のお礼・コメント

弊社の依頼にご提案いただきました皆さま、まことにありがとうございます。
また機会がございましたら、ご参加いただけますこと心よりお願い申し上げます。

```html
<!DOCTYPE html>
<html lang="ja">
<head>
<meta charset="utf-8">
<title>青葉社労士・行政書士</title>
<link href="https://fonts.googleapis.com/css2?family=Noto+Sans+JP:wght@400;500;700&display=swap" rel="stylesheet">
<style>
:root{
  --teal:#5ec5c7;
  --teal-dark:#3aa9ac;
  --teal-pale:#e4f5f5;
  --green:#93c13c;
  --blue:#2a7fc4;
  --ink:#3b4a4c;
  --muted:#8a9a9b;
  --line:#dfe8e8;
  --white:#ffffff;
}
*{margin:0;padding:0;box-sizing:border-box}
html,body{width:886px;height:1200px;overflow:hidden}
body{font-family:"Noto Sans JP",sans-serif;color:var(--ink);background:var(--white);position:relative}
a{color:inherit;text-decoration:none}

.site-header{position:absolute;left:0;top:0;width:886px;height:88px;background:var(--teal-pale)}
.brand{position:absolute;left:22px;top:14px;font-size:14px;font-weight:700;color:var(--teal-dark);display:flex;align-items:center;gap:6px}
.brand-dot{width:10px;height:10px;border-radius:50%;background:var(--teal)}
.header-contact{position:absolute;right:118px;top:8px;text-align:right;color:var(--teal-dark)}
.header-contact small{display:block;font-size:9px}
.header-contact strong{font-size:20px;letter-spacing:1px}
.contact-btn{position:absolute;right:0;top:0;width:108px;height:44px;background:var(--teal);color:var(--white);font-size:11px;display:flex;align-items:center;justify-content:center}
.global-nav{position:absolute;right:20px;top:56px;display:flex;gap:0}
.global-nav a{font-size:11px;color:var(--white);background:var(--teal);padding:6px 14px;border-right:1px solid rgba(255,255,255,.5)}

.hero{position:absolute;left:0;top:88px;width:886px;height:340px;background:linear-gradient(120deg,#7fd3d4,#5ec5c7)}
.hero-photo{position:absolute;left:300px;top:0;width:586px;height:340px;background:linear-gradient(135deg,#f4f6f3 0%,#dde5e2 55%,#c9d6d8 100%);clip-path:polygon(14% 0,100% 0,100% 100%,0 100%)}
.hero-town{position:absolute;left:560px;top:230px;width:326px;height:110px;background:linear-gradient(180deg,#b7cfdc,#9fb3a4)}
.hero-copy{position:absolute;left:560px;top:70px;width:300px;font-size:10.5px;line-height:1.9;color:var(--ink);background:rgba(255,255,255,.7);padding:10px 14px}
.hero-title{position:absolute;left:60px;top:180px;font-size:27px;font-weight:700;line-height:1.55;color:var(--white);background:rgba(58,169,172,.75);padding:6px 18px}
.btn{display:flex;align-items:center;justify-content:center;color:var(--white);font-size:13px;font-weight:700;box-shadow:0 3px 0 rgba(0,0,0,.12)}
.btn-green{background:var(--green)}
.btn-blue{background:var(--blue)}
.hero .btn{position:absolute;top:282px;width:136px;height:38px}

.news{position:absolute;left:60px;top:462px;width:690px}
.news-label{font-size:10px;color:var(--teal-dark);letter-spacing:1px}
.news-title{font-size:26px;font-weight:700;margin-top:2px}
.more-btn{position:absolute;right:0;top:40px;background:var(--teal);color:var(--white);font-size:11px;font-weight:700;padding:4px 12px}
.news-list{list-style:none;margin-top:18px;border-top:1px solid var(--line)}
.news-list li{display:flex;align-items:center;gap:12px;height:35px;border-bottom:1px solid var(--line);font-size:11.5px}
.news-date{color:var(--muted);width:64px}
.tag{font-size:9px;color:var(--white);padding:2px 8px}
.tag-green{background:var(--green)}
.tag-blue{background:var(--blue)}

.site-footer{position:absolute;left:0;top:760px;width:886px;height:440px;background:var(--teal);color:var(--white)}
.office-name{position:absolute;left:60px;top:32px;font-size:17px;font-weight:700}
.office-info{position:absolute;left:60px;top:72px;font-size:10.5px;line-height:1.9}
.office-info p+p{margin-top:8px}
.map{position:absolute;left:540px;top:85px;width:300px;height:175px;background:linear-gradient(135deg,#eef3ee,#d9e6e2)}
.footer-cta{position:absolute;left:260px;top:290px;display:flex;gap:30px}
.footer-cta .btn{width:168px;height:44px;font-size:14px}
.footer-nav{position:absolute;left:0;top:370px;width:886px;display:flex;justify-content:center;gap:34px;font-size:10.5px}
.copyright{position:absolute;left:0;bottom:0;width:886px;height:26px;background:var(--teal-dark);font-size:9px;display:flex;align-items:center;justify-content:center}
</style>
</head>
<body>
<header class="site-header">
  <div class="brand"><span class="brand-dot"></span>青葉社労士・行政書士</div>
  <div class="header-contact"><small>お電話はお気軽にどうぞ（平日 9:00〜18:00）</small><strong>0120-00-1234</strong></div>
  <a class="contact-btn" href="#">お問い合わせ</a>
  <nav class="global-nav">
    <a href="#">事務所概要</a><a href="#">農地転用・農業参入サポート</a><a href="#">社労士サポート</a><a href="#">行政書士サポート</a>
  </nav>
</header>

<section class="hero">
  <div class="hero-photo" role="img" aria-label="書類とペンが置かれた机の写真"></div>
  <div class="hero-town" role="img" aria-label="住宅と田畑が広がる町並みの写真"></div>
  <p class="hero-copy">農地に、住宅地や建物を建てる場合、資材置場、駐車場、太陽光発電設備等、農地以外の目的に転用するには許可が必要です。当事務所では、農地転用から農業参入まで、手続きを丁寧にサポートいたします。</p>
  <h1 class="hero-title">農地転用・農業参入は<br>おまかせください。</h1>
  <a class="btn btn-green" href="#" style="left:64px">農地転用</a>
  <a class="btn btn-blue" href="#" style="left:268px">農業参入</a>
</section>

<section class="news">
  <p class="news-label">NEWS&amp;TOPICS</p>
  <h2 class="news-title">ニュースリリース</h2>
  <a class="more-btn" href="#">MORE ▸</a>
  <ul class="news-list">
    <li><span class="news-date">2020.10.1</span><span class="tag tag-green">農地転用</span>【地域向け】農地転用のご相談会を開催いたします。</li>
    <li><span class="news-date">2020.10.1</span><span class="tag tag-blue">農業参入</span>企業の農業参入のお知らせです。</li>
    <li><span class="news-date">2020.10.1</span><span class="tag tag-blue">お知らせ</span>ホームページをリニューアルしました。</li>
    <li><span class="news-date">2020.10.1</span><span class="tag tag-green">農地転用</span>【地域向け】農地転用のご相談会を開催いたします。</li>
    <li><span class="news-date">2020.10.1</span><span class="tag tag-blue">農業参入</span>企業の農業参入のお知らせです。</li>
    <li><span class="news-date">2020.10.1</span><span class="tag tag-blue">お知らせ</span>ホームページをリニューアルしました。</li>
  </ul>
</section>

<footer class="site-footer">
  <p class="office-name">青葉社労士・行政書士</p>
  <div class="office-info">
    <p>〒000-0000 青葉県緑野市中央町1-2-3 青葉ビル 2F</p>
    <p>社会保険労務士 登録番号 00000000<br>行政書士 登録番号 00000000</p>
    <p>TEL 0120-00-1234　FAX 0120-00-1235</p>
    <p>営業時間<br>平日 9:00〜18:00</p>
  </div>
  <div class="map" role="img" aria-label="事務所周辺の地図"></div>
  <div class="footer-cta">
    <a class="btn btn-green" href="#">農地転用</a>
    <a class="btn btn-blue" href="#">農業参入</a>
  </div>
  <nav class="footer-nav">
    <a href="#">事務所概要</a><a href="#">農地転用・農業参入サポート</a><a href="#">社労士サポート</a><a href="#">行政書士サポート</a><a href="#">お問い合わせ</a>
  </nav>
  <p class="copyright">Copyright © 青葉社労士・行政書士 All Rights Reserved.</p>
</footer>
</body>
</html>
```